Poster Needed for Church Conference

I need a poster for a weekend conference at my church. Looking to attract as many people as possible. We are a church in the suburbs of Houston. This is mainly for our own church members but we are opening it up to outside church members.

Please see previous design from last conference and all other graphic work that can (doesn't need to be) included.

Target Market(s)

It's targeted for all people. But our main audience is families. around the age of 30 should be main target.

Industry/Entity Type

Non-Profit

Font styles to use
Serif
Sans Serif

Colors

Designer to choose colors to be used in the design.

Requirements
Must have
• 11x17 design with ability to shrink and blow up. but ideally for 11x17
• Content and wording:
• "Rooted Lantern Conference: Bridging the gap between generations and passing on our deepest beliefs and values."
• Featuring Dr. Glen Marlowe. Author of "The Map of Q9"
• Aug 25-26: Friday 8-10 pm, Saturday 4-8 pm
• Cost Adults $15/Children $5: Covers admission to all sessions and workshops, refreshments and Saturday dinner. *kids 5 and under free
• Childcare provided for all sessions. "
• Please use church logo and address on flyer: 4312 Orchard Bend, Missouri City, TX 77512
Nice to have
• Ideally it will be designed so that we can crop a 16:9 pp announcement slide and header for our website.
Should not have
• anything offensive

```html
<!DOCTYPE html>
<html lang="en">
<head>
<meta charset="utf-8">
<title>Rooted Lantern Church Conference</title>
<link rel="stylesheet" href="https://fonts.googleapis.com/css2?family=Montserrat:wght@400;500;600;800&family=Yellowtail&display=swap">
<style>
  :root {
    --cream: #f6f2e9;
    --mist: #cfe0db;
    --mist-deep: #a9c7c2;
    --ink: #1d1d1d;
    --text: #2b2b2b;
    --accent-blue: #2fb3d8;
    --accent-orange: #ef6a2c;
    --white: #ffffff;
    --photo-gold: #e9b54a;
    --photo-green: #6f8f3c;
    --photo-deep: #3f5a26;
    --footer: #e4e0da;
  }
  * { margin: 0; padding: 0; box-sizing: border-box; }
  html, body { width: 777px; height: 1200px; overflow: hidden; background: var(--cream); }
  .poster {
    position: relative;
    width: 777px;
    height: 1200px;
    overflow: hidden;
    font-family: "Montserrat", sans-serif;
    color: var(--text);
    text-align: center;
    background:
      radial-gradient(ellipse 260px 420px at 0% 30%, rgba(169,199,194,0.75), transparent 70%),
      radial-gradient(ellipse 260px 420px at 100% 30%, rgba(169,199,194,0.75), transparent 70%),
      radial-gradient(ellipse 500px 220px at 50% 0%, rgba(207,224,219,0.7), transparent 70%),
      linear-gradient(180deg, #eef3ee 0%, var(--cream) 45%, #f2eee6 100%);
  }
  .block { position: absolute; left: 0; width: 100%; }
  .mark-dot {
    position: absolute; left: 358px; top: 86px;
    width: 62px; height: 62px; border-radius: 50%;
    background: var(--accent-blue);
  }
  .title {
    top: 180px;
    font-weight: 800;
    color: var(--ink);
    line-height: 1;
  }
  .title .line-one { display: block; font-size: 60px; letter-spacing: 2px; }
  .title .line-two { display: block; font-size: 54px; letter-spacing: 4px; margin-top: 8px; }
  .subtitle {
    top: 316px;
    font-size: 18px; font-weight: 500;
    letter-spacing: 2.6px; color: var(--ink);
  }
  .tagline {
    top: 354px;
    font-size: 15px; line-height: 19px; letter-spacing: 1.2px;
  }
  .tagline .quote { color: var(--accent-blue); font-weight: 800; font-size: 20px; }
  .featuring {
    top: 440px;
    font-family: "Yellowtail", cursive;
    font-size: 22px; color: var(--accent-orange);
  }
  .speaker {
    top: 477px;
    font-size: 18px; font-weight: 600; letter-spacing: 2.4px; color: var(--ink);
  }
  .book { top: 500px; font-size: 14.5px; letter-spacing: 1.2px; }
  .pill {
    position: absolute;
    background: var(--accent-blue);
    color: var(--white);
    font-weight: 600;
    letter-spacing: 2.6px;
    display: flex; align-items: center; justify-content: center;
  }
  .date-pill { left: 244px; top: 535px; width: 285px; height: 40px; font-size: 17px; }
  .times { top: 586px; font-size: 14.5px; letter-spacing: 1.4px; }
  .price-pill { left: 200px; top: 616px; width: 379px; height: 40px; font-size: 17px; }
  .welcome {
    top: 664px; font-size: 14.5px; font-weight: 600;
    letter-spacing: 1.6px; color: var(--accent-orange);
  }
  .includes { top: 685px; font-size: 14.5px; line-height: 19px; letter-spacing: 1.4px; }
  .note { top: 755px; font-size: 14.5px; line-height: 19px; letter-spacing: 1.4px; }
  .note .childcare { color: var(--accent-orange); font-weight: 600; }
  .family-photo {
    position: absolute; left: 0; top: 836px; width: 777px; height: 212px;
    background:
      radial-gradient(ellipse 260px 180px at 8% 10%, rgba(233,181,74,0.9), transparent 70%),
      radial-gradient(ellipse 300px 160px at 60% 20%, rgba(245,236,200,0.8), transparent 70%),
      linear-gradient(180deg, var(--photo-green) 0%, #8aa24c 55%, var(--photo-deep) 100%);
  }
  .footer {
    position: absolute; left: 0; top: 1048px; width: 777px; height: 152px;
    background: linear-gradient(180deg, #ebe7e1 0%, var(--footer) 100%);
    text-align: left;
  }
  .church-name {
    position: absolute; left: 64px; top: 56px;
    font-size: 17px; font-weight: 500; letter-spacing: 1.4px; color: var(--ink);
    line-height: 21px;
  }
  .address {
    position: absolute; left: 444px; top: 55px;
    font-size: 13px; letter-spacing: 1.4px; line-height: 16px; color: var(--ink);
  }
  .address strong { font-weight: 600; }
</style>
</head>
<body>
  <main class="poster">
    <div class="mark-dot"></div>

    <h1 class="block title">
      <span class="line-one">ROOTED</span>
      <span class="line-two">LANTERN</span>
    </h1>
    <p class="block subtitle">CHURCH CONFERENCE</p>

    <p class="block tagline">
      <span class="quote">“</span> Bridging the gap<br>
      between generations and<br>
      passing on our deepest<br>
      beliefs and values. <span class="quote">”</span>
    </p>

    <p class="block featuring">Featuring</p>
    <p class="block speaker">DR. GLEN MARLOWE</p>
    <p class="block book">Author of ‘The Map of Q9’</p>

    <div class="pill date-pill">AUGUST 25-26 2017</div>
    <p class="block times">Friday 8-10PM, Saturday 4-8PM</p>

    <div class="pill price-pill">ADULTS $15 / CHILDREN $5*</div>
    <p class="block welcome">Non-members are welcome!</p>
    <p class="block includes">
      Covers admission to all sessions<br>
      &amp; workshops.&nbsp; Also includes refreshments<br>
      &amp; Saturday dinner.
    </p>
    <p class="block note">
      *Free for children under 5 years.<br>
      <span class="childcare">Childcare provided for all sessions.</span>
    </p>

    <div class="family-photo" role="img" aria-label="Photo of a young family walking outdoors on a sunlit tree-lined path, parents swinging a toddler between them while another child rides a toy car"></div>

    <footer class="footer">
      <p class="church-name">cedar hollow<br>community church</p>
      <p class="address">
        <strong>CEDAR HOLLOW COMMUNITY CHURCH</strong><br>
        4312 ORCHARD BEND,<br>
        MISSOURI CITY, TX 77512
      </p>
    </footer>
  </main>
</body>
</html>
```